RT Pemberly Electric Yard Sign

Looking to have a yard sign designed that we can place at projects we are working on. Most likely will be 18" H x 24" W but flexible that we can increase the size if necessary. It should include our logo, our phone # 609-555-0147, website rtpemberlyelectric-example.com and slogan, built on integrity, driven by excellence. Colors should match our brand.

```html
<!DOCTYPE html>
<html lang="en">
<head>
<meta charset="utf-8">
<title>RT Pemberly Electric Yard Sign</title>
<link rel="stylesheet" href="https://fonts.googleapis.com/css2?family=Saira+Semi+Condensed:wght@600;700;800&display=swap">
<style>
  :root {
    --navy: #13345a;
    --red: #e5202e;
    --white: #ffffff;
    --backdrop: #eceef0;
  }
  * { margin: 0; padding: 0; box-sizing: border-box; }
  html, body {
    width: 1200px;
    height: 1029px;
    overflow: hidden;
    background: var(--backdrop);
  }
  .yard-sign {
    position: absolute;
    left: 0;
    top: 64px;
    width: 1200px;
    height: 901px;
    overflow: hidden;
    font-family: "Saira Semi Condensed", "Arial Narrow", sans-serif;
  }
  .sign-art {
    position: absolute;
    inset: 0;
    width: 1200px;
    height: 901px;
  }
  .brand,
  .slogan,
  .contact-phone,
  .contact-web {
    position: absolute;
    text-align: center;
    white-space: nowrap;
    line-height: 1;
  }
  .brand { left: 360px; width: 790px; }
  .brand-mark {
    position: absolute;
    left: 723px;
    top: 44px;
    width: 64px;
    height: 64px;
    border-radius: 50%;
    background: var(--red);
  }
  .brand-name {
    top: 150px;
    font-size: 84px;
    font-weight: 800;
    letter-spacing: 5px;
    text-transform: uppercase;
    color: var(--red);
  }
  .brand-trade {
    top: 280px;
    font-size: 42px;
    font-weight: 700;
    letter-spacing: 6px;
    color: var(--navy);
  }
  .slogan {
    left: 360px;
    top: 424px;
    width: 790px;
    color: var(--white);
    font-size: 60px;
    font-weight: 700;
    line-height: 76px;
  }
  .slogan-line { display: block; }
  .slogan-line--ruled {
    display: flex;
    align-items: center;
    justify-content: center;
    gap: 32px;
  }
  .slogan-rule {
    width: 124px;
    height: 4px;
    background: var(--white);
    clip-path: polygon(0 50%, 8% 0, 100% 0, 100% 100%, 8% 100%);
  }
  .slogan-rule--right { clip-path: polygon(0 0, 92% 0, 100% 50%, 92% 100%, 0 100%); }
  .contact-phone {
    left: 320px;
    top: 640px;
    width: 840px;
    color: var(--white);
    font-size: 108px;
    font-weight: 800;
    letter-spacing: 2px;
  }
  .contact-web {
    left: 300px;
    top: 790px;
    width: 880px;
    color: var(--white);
    font-size: 38px;
    font-weight: 700;
    letter-spacing: 1px;
  }
</style>
</head>
<body>
<main class="yard-sign">
  <svg class="sign-art" viewBox="0 0 1200 901" aria-hidden="true">
    <rect class="panel-top" x="0" y="0" width="1200" height="400" fill="var(--white)"/>
    <rect class="band-slogan" x="0" y="400" width="1200" height="202" fill="var(--navy)"/>
    <rect class="band-contact" x="0" y="602" width="1200" height="299" fill="var(--red)"/>
    <polygon class="side-panel" points="0,0 430,0 150,901 0,901" fill="var(--navy)"/>
    <polygon class="side-stripe-white" points="392,0 430,0 150,901 112,901" fill="var(--white)"/>
    <polygon class="side-stripe-red" points="330,90 356,90 92,901 60,901" fill="var(--red)"/>
    <rect class="trade-rule-red" x="375" y="342" width="770" height="5" fill="var(--red)"/>
    <rect class="trade-rule-navy" x="385" y="348" width="750" height="6" fill="var(--navy)"/>
  </svg>

  <span class="brand-mark" aria-hidden="true"></span>
  <h1 class="brand brand-name">RT Pemberly</h1>
  <p class="brand brand-trade">Electrical Contractor</p>

  <p class="slogan">
    <span class="slogan-line">Built on Integrity, Driven</span>
    <span class="slogan-line slogan-line--ruled">
      <span class="slogan-rule"></span>by Excellence<span class="slogan-rule slogan-rule--right"></span>
    </span>
  </p>

  <p class="contact-phone">609-555-0147</p>
  <p class="contact-web">www.rtpemberlyelectric-example.com</p>
</main>
</body>
</html>
```